Wander Through Maple Valley - Book Cover

I am looking for a FRONT and BACK cover for my new book. It is going to be Christian Coloring Book for Adults so I want it to be eye-catching, friendly and very pretty. The title is: Wander Through Maple Valley. I would like for the following words to be bigger than the rest in the tite: Color, Word, Lord. This is to create more emphasis.
I will attach two pictures that will be in the book, you are welcome to use any part o the images to make the cover better. Keep in mind these are coloring pages so if you're going to use them PLEASE color them in. I want vibrant, eye-catching colors but with a nice contrast. The title should be easy to read from a thumbnail size, no real images on covers, original work ONLY and do NOT include author on the front cover.
Let me know if you have any questions. Good luck :)

```html
<!DOCTYPE html>
<html lang="en">
<head>
<meta charset="utf-8">
<title>Wander Through Maple Valley – Book Cover</title>
<link rel="stylesheet" href="https://fonts.googleapis.com/css2?family=Almendra:wght@700&display=swap">
<style>
  :root {
    --paper: #ffffff;
    --magenta: #e8359a;
    --violet: #8a3df0;
    --blue: #3fa6f2;
    --cyan: #3ee0e6;
    --green: #6ee65a;
    --orange: #ff7a1a;
    --red: #f0303c;
    --gold-light: #f3d48a;
    --gold: #c8963e;
    --gold-dark: #8a5a1c;
    --medallion: #f7f7f7;
  }
  * { margin: 0; padding: 0; box-sizing: border-box; }
  html, body { width: 1192px; height: 1200px; overflow: hidden; background: var(--paper); }
  .cover {
    position: relative;
    width: 1192px;
    height: 1200px;
    overflow: hidden;
    background: var(--paper);
  }
  .mandala {
    position: absolute;
    border-radius: 50%;
    -webkit-mask: radial-gradient(circle, #000 0 58%, transparent 59% 62%, #000 63% 100%);
            mask: radial-gradient(circle, #000 0 58%, transparent 59% 62%, #000 63% 100%);
    opacity: 0.85;
  }
  .mandala--center {
    left: 126px; top: 132px; width: 940px; height: 940px;
    background: conic-gradient(from 0deg, var(--violet), var(--magenta), var(--red), var(--orange), var(--orange), var(--magenta), var(--violet), var(--blue), var(--cyan), var(--green), var(--green), var(--cyan), var(--violet));
  }
  .mandala--top-left {
    left: -165px; top: -172px; width: 556px; height: 556px;
    background: conic-gradient(from 0deg, var(--magenta), var(--red), var(--orange), var(--magenta), var(--violet), var(--blue), var(--violet), var(--magenta));
  }
  .mandala--top-right {
    left: 801px; top: -172px; width: 556px; height: 556px;
    background: conic-gradient(from 0deg, var(--green), var(--cyan), var(--blue), var(--cyan), var(--green), var(--green), var(--green));
  }
  .mandala--bottom-left {
    left: -172px; top: 808px; width: 556px; height: 556px;
    background: conic-gradient(from 0deg, var(--red), var(--orange), var(--orange), var(--magenta), var(--magenta), var(--red));
  }
  .mandala--bottom-right {
    left: 801px; top: 814px; width: 556px; height: 556px;
    background: conic-gradient(from 0deg, var(--violet), var(--blue), var(--cyan), var(--green), var(--cyan), var(--blue), var(--violet));
  }
  .medallion {
    position: absolute;
    left: 311px; top: 317px;
    width: 570px; height: 570px;
    border-radius: 50%;
    background: radial-gradient(circle at 45% 40%, #ffffff 0%, var(--medallion) 100%);
    box-shadow: 0 4px 14px rgba(0,0,0,0.18), 0 0 0 6px rgba(255,255,255,0.9);
  }
  .title {
    position: absolute;
    left: 311px; top: 317px;
    width: 570px; height: 570px;
    display: flex;
    flex-direction: column;
    align-items: center;
    justify-content: center;
    font-family: "Almendra", Georgia, serif;
    font-weight: 700;
    text-transform: uppercase;
    line-height: 1;
    text-align: center;
  }
  .title__line {
    display: block;
    background: linear-gradient(180deg, var(--gold-light) 0%, var(--gold) 45%, var(--gold-dark) 70%, var(--gold) 100%);
    -webkit-background-clip: text;
            background-clip: text;
    color: transparent;
    filter: drop-shadow(1px 1px 0 rgba(90,60,20,0.25));
  }
  .title__line--major { font-size: 92px; letter-spacing: 1px; margin: 6px 0; }
  .title__line--minor { font-size: 48px; letter-spacing: 2px; margin: 8px 0; }
</style>
</head>
<body>
  <main class="cover">
    <div class="mandala mandala--top-left" role="img" aria-label="Colourful mandala ornament in magenta, orange and violet"></div>
    <div class="mandala mandala--top-right" role="img" aria-label="Colourful mandala ornament in green, cyan and blue"></div>
    <div class="mandala mandala--bottom-left" role="img" aria-label="Colourful mandala ornament in red, orange and magenta"></div>
    <div class="mandala mandala--bottom-right" role="img" aria-label="Colourful mandala ornament in violet, blue and green"></div>
    <div class="mandala mandala--center" role="img" aria-label="Large rainbow mandala ornament framing the title"></div>
    <div class="medallion"></div>
    <h1 class="title">
      <span class="title__line title__line--major">Wander</span>
      <span class="title__line title__line--minor">Through</span>
      <span class="title__line title__line--major">Maple</span>
      <span class="title__line title__line--major">Valley</span>
    </h1>
  </main>
</body>
</html>
```